letterhead design for a investing company*

Design an appealing business letterhead to match with our existing logo and attract new customers. Our customers are mainly corporate managers which are detail oriented and judge the company ability to perform a good service based on small details. A professional letterhead will give a good first impression.

Target Market(s)

New customers and business owners

Industry/Entity Type

Marketplace

Font styles to use
Sans Serif
Script

Requirements
Must have
• Must be a professional and elegant design that attracts interest from people who receives it

```html
<!DOCTYPE html>
<html lang="en">
<head>
<meta charset="utf-8">
<title>Brightvale Letterhead</title>
<link href="https://fonts.googleapis.com/css2?family=Montserrat:wght@400;500;600;800&family=Allura&display=swap" rel="stylesheet">
<style>
  :root{
    --navy:#232d4f;
    --gold:#e8ae1c;
    --ink:#3a3d45;
    --paper:#ffffff;
    --backdrop:#ececec;
    --mark:#eef0f3;
  }
  *{margin:0;padding:0;box-sizing:border-box}
  html,body{width:1200px;height:900px;overflow:hidden;background:var(--backdrop)}
  body{display:flex;align-items:center;justify-content:center;font-family:"Montserrat",sans-serif}
  .letterhead{position:relative;width:600px;height:849px;background:var(--paper);box-shadow:0 2px 10px rgba(0,0,0,.08);overflow:hidden}
  .header-rule-left{position:absolute;left:0;top:106px;width:40px;height:8px;background:var(--navy)}
  .brand{position:absolute;left:58px;top:88px;display:flex;align-items:center;gap:10px}
  .brand-dot{width:26px;height:26px;border-radius:50%;background:var(--gold)}
  .brand-name{font-weight:800;font-size:34px;color:var(--navy);letter-spacing:.2px;line-height:1}
  .header-rule-right{position:absolute;left:292px;right:0;top:98px;height:8px;background:var(--gold)}
  .backdrop-mark{position:absolute;left:190px;top:250px;width:300px;height:300px;border-radius:50%;background:var(--mark)}
  .letter-body{position:absolute;left:60px;top:205px;width:470px;font-size:10.6px;line-height:1.45;color:var(--ink)}
  .letter-body p{margin-bottom:14px}
  .signoff{position:absolute;left:92px;top:560px}
  .signature{font-family:"Allura",cursive;font-size:34px;color:#2b3bb0;line-height:1}
  .role{font-size:11px;color:var(--ink);margin-left:16px}
  .contact{position:absolute;right:150px;top:728px;text-align:right;font-size:10.5px;font-weight:600;color:var(--navy);line-height:1.8}
  .contact .label{color:var(--gold);margin-left:6px}
  .footer-rule{position:absolute;left:0;width:455px;top:772px;height:3px;background:var(--gold)}
  .social-tab{position:absolute;right:0;top:758px;width:140px;height:30px}
  .social-tab svg{position:absolute;inset:0}
  .social-handle{position:absolute;left:30px;top:8px;font-size:11px;font-weight:500;color:#fff}
</style>
</head>
<body>
  <main class="letterhead">
    <div class="backdrop-mark" aria-hidden="true"></div>

    <div class="header-rule-left"></div>
    <div class="brand">
      <span class="brand-dot"></span>
      <span class="brand-name">Brightvale</span>
    </div>
    <div class="header-rule-right"></div>

    <section class="letter-body">
      <p>Letterhead samples are a great way of deciding what kind of letterhead you want to design for you and your company. The internet has a ton of great letterhead samples to browse through. Whether you want something simple, with just a couple lines of text of your business information, or something decorative and stunning, with photos and logos on the top and bottom of the page, it will be easy to find what you want, because there are samples online for basically any type of letterhead you could want.</p>
      <p>Any business could easily benefit from browsing through some letterhead samples, if only to get an idea for what kind of letterhead their company might want. Letterheads are just one of the tools that a business professional could use to help increase their customer base, and to really be memorable to everyone they write a letter to. Letterhead is quite an effective tool for marketing and advertising, but because it's such a simple and well known idea, it is often unfairly overlooked. Make sure you don't make that mistake, and make some letterhead samples of your own today.</p>
      <p>Whether you want to get new customers to remember you and become part of your clientele, or you just want to send out friendly reminders to your existing clients, customizing your own letterhead samples can really help you out. Try out some letterhead samples and you will not regret it, and I'm sure you will add a new tool to your business' arsenal of networking, marketing, and advertising tools.</p>
    </section>

    <div class="signoff">
      <div class="signature">Daniel Harlow</div>
      <div class="role">company director</div>
    </div>

    <address class="contact" style="font-style:normal">
      <div>48 Sample Road, Midtown, New York 10001</div>
      <div><span class="label">P:</span> 555 010 20 30 <span class="label">M:</span> 555 010 40 50 <span class="label">E:</span> info@brightvale.com</div>
    </address>

    <div class="footer-rule"></div>
    <div class="social-tab">
      <svg width="140" height="30" viewBox="0 0 140 30"><polygon points="0,15 14,0 140,0 140,30 14,30" fill="#232d4f"/></svg>
      <span class="social-handle">@brightvale</span>
    </div>
  </main>
</body>
</html>
```